UK young peoples' debating organisation needs flyers for tournament + promotion for major club laun

I need a flyer for the tournament but also sell the after-school clubs on offer.

Needs to be modern, energetic and fun, challenging the traditional idea of debating as simply academic and elitist.

Must appeal to busy headteachers as well as parents and children.

Target Market(s)

Headteachers; children aged 8 - 11 and their parents

Industry/Entity Type

Education

Font styles to use
Serif
Decorative

Colors

Designer to choose colors to be used in the design.

Requirements
Must have
• The Brightwell Oratory logo, plus the Harrowmere Borough Council Logo. The text attached on word doc. (writing in brackets and italics are directions, not to be included as text).
• A space theme (rockets? Stars?/ relates to Brightwell. Ideas of movement, aspiration, aiming high etc.
Nice to have
Should not have
• anything relating to pure academia and tradition (mortar boards, suits and ties etc); mo

```html
<!DOCTYPE html>
<html lang="en">
<head>
<meta charset="utf-8">
<title>Brightwell Oratory – Tournament and Clubs Flyers</title>
<link rel="stylesheet" href="https://fonts.googleapis.com/css2?family=Roboto+Condensed:wght@700&family=Open+Sans:wght@400;600;700&display=swap">
<style>
  :root {
    --red: #b3151b;
    --orange: #e8821c;
    --ink: #3a3a3a;
    --body: #333333;
    --paper: #f6f6f6;
    --backdrop: #e9e4dc;
    --footer-light: #ececec;
    --footer-dark: #bdbdbd;
    --swoosh-dark: #3d3d3d;
    --photo-warm-a: #c9a98c;
    --photo-warm-b: #5a4a45;
    --photo-cool-a: #e8ecef;
    --photo-cool-b: #6b7480;
    --badge: #2a63b8;
  }
  * { box-sizing: border-box; margin: 0; padding: 0; }
  html, body { width: 1200px; height: 1000px; overflow: hidden; }
  body { background: var(--backdrop); position: relative; font-family: "Open Sans", Arial, sans-serif; color: var(--body); }

  .flyer {
    position: absolute; top: 117px; width: 542px; height: 766px;
    background: var(--paper); overflow: hidden;
    box-shadow: 6px 8px 14px rgba(0,0,0,.35);
  }
  .flyer--tournament { left: 43px; }
  .flyer--clubs { left: 615px; }

  .top-bar { position: absolute; top: 0; left: 0; width: 100%; height: 14px; display: flex; }
  .top-bar__red { width: 50%; background: var(--red); }
  .top-bar__orange { width: 50%; background: var(--orange); }

  .photo { position: absolute; top: 14px; left: 0; width: 100%; height: 360px; }
  .flyer--tournament .photo { background: linear-gradient(180deg, #d9d4cc 0%, var(--photo-warm-a) 40%, var(--photo-warm-b) 100%); }
  .flyer--clubs .photo { background: linear-gradient(90deg, #3b3430 0%, var(--photo-cool-b) 22%, var(--photo-cool-a) 60%, var(--photo-cool-b) 100%); }

  .shapes { position: absolute; top: 0; left: 0; width: 542px; height: 766px; }

  .copy { position: absolute; left: 0; width: 100%; text-align: center; }

  .invite {
    top: 408px; font-family: "Roboto Condensed", "Arial Narrow", sans-serif;
    font-weight: 700; font-size: 19px; line-height: 22px; color: var(--orange);
  }
  .launch { top: 460px; font-weight: 700; font-size: 22px; line-height: 30px; color: var(--ink); }
  .launch em { font-style: normal; color: var(--red); }
  .details { font-size: 9.6px; line-height: 12.5px; color: var(--body); padding: 0 40px; }
  .details--first { top: 492px; }
  .finals { top: 535px; font-weight: 700; font-size: 15px; line-height: 20px; color: var(--red); }
  .details--second { top: 558px; }
  .details a { color: var(--red); font-weight: 700; text-decoration: none; }

  .call { font-weight: 700; line-height: 23px; }
  .call__label { display: block; font-size: 21px; color: var(--ink); }
  .call__number { display: block; font-size: 21px; color: var(--red); }
  .flyer--tournament .call { top: 629px; }

  .brand { position: absolute; display: flex; align-items: center; gap: 6px; }
  .brand__dot { width: 22px; height: 22px; border-radius: 50%; background: var(--red); }
  .brand__name { font-weight: 600; font-size: 12.5px; color: var(--ink); }
  .flyer--tournament .brand { left: 40px; top: 718px; }
  .flyer--clubs .brand { left: 42px; top: 722px; }
  .brand__tagline { position: absolute; left: 16px; top: 748px; font-size: 7px; color: var(--ink); }

  .web-link { position: absolute; left: 226px; top: 734px; display: flex; align-items: center; gap: 6px; font-size: 9px; color: var(--red); }
  .web-link__icon { width: 10px; height: 10px; border-radius: 50%; border: 2px solid var(--red); }

  .council-badge {
    position: absolute; width: 64px; height: 64px; border-radius: 50%;
    background: #fff; border: 4px solid var(--badge);
  }
  .flyer--tournament .council-badge { left: 451px; top: 684px; }
  .flyer--clubs .council-badge { left: 451px; top: 684px; }

  .headline {
    top: 398px; left: 50px; text-align: left; width: auto;
    font-family: "Roboto Condensed", "Arial Narrow", sans-serif;
    font-weight: 700; font-size: 21px; color: var(--red); letter-spacing: .2px;
  }
  .body-copy { top: 432px; left: 55px; width: 440px; text-align: left; font-size: 9.4px; line-height: 12.4px; }
  .body-copy p + p { margin-top: 12.4px; }
  .find-out { top: 636px; font-size: 14px; color: var(--ink); }
  .find-out a { color: var(--red); font-weight: 700; text-decoration: none; }
  .flyer--clubs .call { top: 709px; }
</style>
</head>
<body>

<section class="flyer flyer--tournament">
  <div class="top-bar"><span class="top-bar__red"></span><span class="top-bar__orange"></span></div>
  <div class="photo" role="img" aria-label="Photo of a large audience seated in a lecture hall facing a projection screen"></div>
  <svg class="shapes" viewBox="0 0 542 766" aria-hidden="true">
    <path d="M0,300 Q250,395 542,290 L542,766 L0,766 Z" fill="#b3151b"/>
    <path d="M100,372 Q330,400 542,305 L542,766 L0,766 Z" fill="#e8821c"/>
    <path d="M0,325 Q270,405 542,318 L542,766 L0,766 Z" fill="#f6f6f6"/>
    <path d="M0,655 Q280,725 542,628 L542,766 L0,766 Z" fill="#3d3d3d"/>
    <defs><linearGradient id="footGradA" x1="0" y1="0" x2="0" y2="1"><stop offset="0" stop-color="#ececec"/><stop offset="1" stop-color="#bdbdbd"/></linearGradient></defs>
    <path d="M0,664 Q280,734 542,640 L542,766 L0,766 Z" fill="url(#footGradA)"/>
  </svg>

  <p class="copy invite">You are warmly invited to attend the first<br>Harrowmere Primary Schools Brightwell Debating Tournament!</p>
  <p class="copy launch">It all blasts off on <em>21st June at 9:30am,</em></p>
  <p class="copy details details--first">when 10 teams of Year 4s and 5s battle it out,<br>critically discussing controversial topics with articulacy and confidence.<br>The 4 most persuasive and responsive teams will then skyrocket into the semis and finals on</p>
  <p class="copy finals">29th June from 12:30pm.</p>
  <p class="copy details details--second">All debates are held at Ashcombe School, Mill Road, Harrowmere HM4 2EE.<br>Come and see how far and fast our Key Stage 2 pupils have travelled.<br>We’ll be launching our unique, progression-based after-school clubs for primary schools at this event.<br>Zoom over at any time. We’re committed to safeguarding our intrepid debaters, so please RSVP to<br><a>info@brightwelloratory.org</a> with day and time of attendance, or with any queries.</p>
  <p class="copy call"><span class="call__label">CALL US</span><span class="call__number">07700 900 418</span></p>

  <div class="brand"><span class="brand__dot"></span><span class="brand__name">Brightwell Oratory</span></div>
  <p class="brand__tagline">Promoting debating skills for all young people</p>
  <p class="web-link"><span class="web-link__icon"></span>www.brightwelloratory.org</p>
  <div class="council-badge" role="img" aria-label="Harrowmere Borough Council badge"></div>
</section>

<section class="flyer flyer--clubs">
  <div class="top-bar"><span class="top-bar__red"></span><span class="top-bar__orange"></span></div>
  <div class="photo" role="img" aria-label="Photo of a microphone in front of a blurred seated panel"></div>
  <svg class="shapes" viewBox="0 0 542 766" aria-hidden="true">
    <path d="M0,300 Q250,395 542,290 L542,766 L0,766 Z" fill="#b3151b"/>
    <path d="M100,372 Q330,400 542,305 L542,766 L0,766 Z" fill="#e8821c"/>
    <path d="M0,325 Q270,405 542,318 L542,766 L0,766 Z" fill="#f6f6f6"/>
    <path d="M0,648 Q300,700 542,630 L542,766 L0,766 Z" fill="#3d3d3d"/>
    <defs><linearGradient id="footGradB" x1="0" y1="0" x2="0" y2="1"><stop offset="0" stop-color="#ececec"/><stop offset="1" stop-color="#bdbdbd"/></linearGradient></defs>
    <path d="M0,660 Q300,708 542,642 L542,766 L0,766 Z" fill="url(#footGradB)"/>
  </svg>

  <h2 class="copy headline">CALLING ALL PRIMARY AND PREP SCHOOLS</h2>
  <div class="copy body-copy">
    <p>Give your children the skills to speak confidently, think critically and expand their horizons. Give your teachers the chance to lead them.</p>
    <p>We’ve devised a weekly programme to ensure debating becomes a truly enriching part of your school’s culture. Clubs are progression-based and teach skills explicitly each week. They allow control of learning to be in pupils’ hands, using specifically-designed debating notebooks and stickers for each child to encourage reflection, research and full participation.</p>
    <p>Our programme is fun, challenging and varied. It also upskills teachers keen to take their pupils’ debating to the next level. We’re always on hand to help online, or in person where possible. By the end of the year we’ll ensure we visit you for a day to help you embed debating into your curriculum. You can also opt to enter your pupils for the Level 1 Debating qualification from the National Speech Board, for which they will be fully prepared.</p>
    <p>We’re committed to access for all, so please contact for pricing options.</p>
  </div>
  <p class="copy find-out">Find out more at <a>www.brightwelloratory.org</a></p>
  <p class="copy call"><span class="call__label">CALL US</span><span class="call__number">07700 900 418</span></p>

  <div class="brand"><span class="brand__dot"></span><span class="brand__name">Brightwell Oratory</span></div>
  <div class="council-badge" role="img" aria-label="Harrowmere Borough Council badge"></div>
</section>

</body>
</html>
```